Web Design for a recruitment company

Website is for a recruitment company, with a particular focus on temporary staff, trades, skilled, and unskilled labour markets. Website will consist of a home page design and separate design for additional pages. Website will be implemented as a template in SharePoint. There is a separate design project for a new logo and look colours will need to be co-ordinated.

Target Market(s)

Company executives in the construction and trades areas looking for staff. Trades people, skilled and unskilled labourers looking for work.

Industry/Entity Type

It Company

Number of Pages Required

2 page

Requirements
Must have
• Looking for Home Page design plus design for additional pages.
• .
Nice to have
• Good Crew | Good Site is the firms byline, company name is TOV Staffing. They will be in the Logo (separate project) but may also appear elsewhere in the design.
• Company values (attached file) may be reflected in the design where practical.

```html
<!DOCTYPE html>
<html lang="en">
<head>
<meta charset="utf-8">
<title>TOV Staffing</title>
<link rel="stylesheet" href="https://fonts.googleapis.com/css2?family=Open+Sans:wght@400;600;700&family=Raleway:wght@400;500&family=Roboto+Slab:wght@400;700&display=swap">
<style>
:root{
  --yellow:#f2c21b;
  --yellow-dark:#e6b612;
  --ink:#2b2b2b;
  --grey-text:#8a8a8a;
  --band:#ececec;
  --footer:#1e1e1e;
  --footer-bottom:#141414;
  --white:#ffffff;
}
*{box-sizing:border-box;margin:0;padding:0}
html,body{width:829px;height:1200px;overflow:hidden;background:var(--white)}
body{position:relative;font-family:"Open Sans",Arial,sans-serif;color:var(--ink)}
.top-stripe{position:absolute;left:0;top:0;width:829px;height:4px;background:var(--yellow)}
.site-header{position:absolute;left:0;top:4px;width:829px;height:52px;background:var(--white)}
.brand{position:absolute;left:45px;top:12px;display:flex;align-items:center;gap:8px}
.brand-dot{width:26px;height:26px;border-radius:50%;background:#3a3a3a}
.brand-name{font-family:"Roboto Slab",Georgia,serif;font-weight:700;font-size:17px;line-height:18px;color:var(--ink)}
.brand-tag{font-family:"Open Sans",Arial,sans-serif;font-size:8.5px;color:#555;line-height:11px}
.main-nav{position:absolute;top:16px;left:457px;display:flex;font-family:"Roboto Slab",Georgia,serif;font-size:10.5px;color:#666}
.main-nav a{display:block;height:24px;line-height:24px;padding:0 12px;text-decoration:none;color:#666}
.main-nav a.active{background:var(--yellow);color:#333}
.hero{position:absolute;left:0;top:56px;width:829px;height:255px;background:linear-gradient(180deg,#d8c3a6 0%,#b08a63 45%,#5b4430 100%)}
.hero-arrow{position:absolute;top:102px;width:50px;height:50px;border-radius:50%;background:rgba(80,80,80,.7)}
.hero-arrow.prev{left:16px}
.hero-arrow.next{right:0;background:transparent}
.hero-caption{position:absolute;left:40px;top:196px;color:var(--white);width:270px}
.hero-caption h2{font-family:"Open Sans",Arial,sans-serif;font-weight:400;font-size:13px;margin-bottom:4px}
.hero-caption p{font-size:9px;line-height:12px}
.section-title{position:absolute;left:47px;top:336px;font-family:"Raleway",Arial,sans-serif;font-size:15px;letter-spacing:.3px;color:#333}
.section-title::before{content:"";position:absolute;left:0;top:-3px;width:38px;height:2px;background:var(--yellow)}
.service{position:absolute;top:371px;width:180px;text-align:center}
.service-photo{width:114px;height:114px;border-radius:50%;margin:0 auto;border:4px solid #eee;box-shadow:0 0 0 1px #ddd}
.service h3{font-family:"Raleway",Arial,sans-serif;font-weight:500;font-size:15px;margin-top:23px;letter-spacing:.3px}
.service p{font-size:10.5px;line-height:16px;color:var(--grey-text);margin-top:8px;padding:0 10px}
.btn{display:inline-block;margin-top:20px;width:97px;height:25px;line-height:25px;background:var(--yellow);color:var(--white);font-size:9.5px;font-weight:600;text-decoration:none}
.band{position:absolute;left:0;top:661px;width:829px;height:175px;background:var(--band)}
.card{position:absolute;top:680px;width:236px;height:133px}
.news-card{left:41px;background:#2f3236;color:#ddd;padding:16px 12px}
.news-card h4{font-family:"Open Sans",Arial,sans-serif;font-weight:400;font-size:13px;color:var(--white);padding-bottom:6px;border-bottom:2px solid transparent;position:relative}
.news-card h4::after{content:"";position:absolute;left:0;bottom:-2px;width:212px;height:1px;background:var(--yellow)}
.news-card p{font-size:9px;line-height:15px;margin-top:14px}
.photo-card .label{position:absolute;left:0;bottom:0;width:100%;height:26px;border-top:2px solid var(--yellow);background:rgba(20,20,20,.55);color:var(--white);font-size:12.5px;line-height:24px;padding-left:7px}
.cta{position:absolute;left:0;top:836px;width:829px;height:112px;background:var(--yellow);text-align:center;color:var(--white)}
.cta-line{font-family:"Roboto Slab",Georgia,serif;font-size:16px;line-height:18px}
.cta-line:first-child{margin-top:24px}
.cta-phone{font-family:"Open Sans",Arial,sans-serif;font-weight:700;font-size:25px;color:#333;margin-top:2px}
.site-footer{position:absolute;left:0;top:948px;width:829px;height:221px;background:var(--footer)}
.footer-col{position:absolute;top:36px;color:#bbb}
.footer-col h5{font-family:"Open Sans",Arial,sans-serif;font-weight:400;font-size:12px;color:var(--white);margin-bottom:12px}
.footer-col li{list-style:none;font-size:9px;height:22.6px}
.social li{display:flex;align-items:center;gap:10px;height:34px;font-size:10.5px}
.social-dot{width:22px;height:22px;border-radius:50%;background:var(--white)}
.footer-bottom{position:absolute;left:0;top:1169px;width:829px;height:31px;background:var(--footer-bottom);color:var(--white);font-size:8.5px;line-height:31px}
.footer-bottom nav{position:absolute;left:49px}
.footer-bottom nav span{margin:0 6px}
.footer-bottom .copy{position:absolute;right:41px}
</style>
</head>
<body>
<div class="top-stripe"></div>
<header class="site-header">
  <div class="brand">
    <div class="brand-dot"></div>
    <div>
      <div class="brand-name">TOV Staffing</div>
      <div class="brand-tag">Good Crew | Good Site</div>
    </div>
  </div>
  <nav class="main-nav">
    <a class="active">HOME</a><a>COMPANY</a><a>BRANDS</a><a>PRODUCTS</a><a>CONTACTS</a>
  </nav>
</header>

<section class="hero" role="img" aria-label="Workers with a drilling rig on a hillside at sunset">
  <div class="hero-arrow prev">
    <svg width="50" height="50" viewBox="0 0 50 50"><path d="M28 17 L20 25 L28 33" stroke="#222" stroke-width="2.5" fill="none"/></svg>
  </div>
  <div class="hero-arrow next" style="top:102px;width:40px">
    <svg width="40" height="50" viewBox="0 0 40 50"><path d="M15 18 L22 25 L15 32" stroke="#f2c21b" stroke-width="2.5" fill="none"/></svg>
  </div>
  <div class="hero-caption">
    <h2>TOV Staffing</h2>
    <p>Nullam quis risus eget urna mollis ornare vel eu leo. Curabitur blandit tempus porttitor. Cum sociis natoque penatibus et</p>
  </div>
</section>

<h2 class="section-title">SERVICES</h2>

<article class="service" style="left:38px">
  <div class="service-photo" role="img" aria-label="Worker using a laptop" style="background:radial-gradient(circle,#c9733a,#5a3a25)"></div>
  <h3>DATA MANAGEMENT</h3>
  <p>Lorem ipsum dolor sit amet, consectetur adipiscing elit. Nulla mollis, neque sed rutrum mollis, augue leo suscipit lectus, sit amet</p>
  <a class="btn">READ MORE &#187;</a>
</article>
<article class="service" style="left:229px">
  <div class="service-photo" role="img" aria-label="Welder at work with sparks" style="background:radial-gradient(circle,#b8913e,#2a2418)"></div>
  <h3>PLANTING</h3>
  <p>Lorem ipsum dolor sit amet, consectetur adipiscing elit. Nulla mollis, neque sed rutrum mollis, augue leo suscipit lectus, sit amet</p>
  <a class="btn">READ MORE &#187;</a>
</article>
<article class="service" style="left:421px">
  <div class="service-photo" role="img" aria-label="Red valve wheel on pipework" style="background:radial-gradient(circle,#9a3a2a,#3a2e28)"></div>
  <h3>HARVEST</h3>
  <p>Lorem ipsum dolor sit amet, consectetur adipiscing elit. Nulla mollis, neque sed rutrum mollis, augue leo suscipit lectus, sit amet</p>
  <a class="btn">READ MORE &#187;</a>
</article>
<article class="service" style="left:613px">
  <div class="service-photo" role="img" aria-label="Metal grinding with bright sparks" style="background:radial-gradient(circle,#7fa6d0,#1e2638)"></div>
  <h3>APPLICATION</h3>
  <p>Lorem ipsum dolor sit amet, consectetur adipiscing elit. Nulla mollis, neque sed rutrum mollis, augue leo suscipit lectus, sit amet</p>
  <a class="btn">READ MORE &#187;</a>
</article>

<div class="band"></div>
<article class="card news-card">
  <h4>Recent News</h4>
  <p>Ut lobortis, nisl eu adipiscing tristique, lectus justo luctus massa, ultricies viverra eros metus eu tellus. Cum sociis natoque penatibus et magnis dis parturient montes, nascetur ridiculus mus.</p>
</article>
<article class="card photo-card" style="left:296px;background:linear-gradient(160deg,#3d4a3a,#1c1a16 60%,#7a5a2a)" role="img" aria-label="Welder working in a workshop">
  <div class="label">Lorem Ipsum Dolor</div>
</article>
<article class="card photo-card" style="left:552px;background:linear-gradient(150deg,#d8cf98,#9a8c5a 55%,#4a4438)" role="img" aria-label="Close view of a circuit board">
  <div class="label">Lorem Ipsum Dolor</div>
</article>

<section class="cta">
  <div class="cta-line">CALL A REGISTERED</div>
  <div class="cta-line">TOV STAFFING</div>
  <div class="cta-phone">1 200 555 0148</div>
</section>

<footer class="site-footer">
  <div class="footer-col" style="left:47px">
    <h5>PRODUCTS</h5>
    <ul><li>Equipment</li><li>Industry Solutions</li><li>Power Systems</li><li>Attachments</li><li>Rental Equipment - HireYardStore.com</li><li>Used Equipment - YardUsed.com</li></ul>
  </div>
  <div class="footer-col" style="left:236px">
    <h5>SUPPORT</h5>
    <ul><li>Protect Your Investment</li><li>Operate Efficiently and Safely</li><li>Maintenance &amp; Support</li><li>Financing &amp; Insurance</li><li>Find Your Dealer</li><li>Contact Us</li></ul>
  </div>
  <div class="footer-col" style="left:427px">
    <h5>NEWS AND EVENTS</h5>
    <ul><li>Product &amp; Service Announcements</li><li>Press Kits</li><li>Trade Shows &amp; Events</li></ul>
  </div>
  <div class="footer-col social" style="left:617px">
    <h5>SOCIAL</h5>
    <ul><li><span class="social-dot"></span>Crewbook</li><li><span class="social-dot"></span>Chirper</li></ul>
  </div>
</footer>
<div class="footer-bottom">
  <nav>Home<span>|</span>Company<span>|</span>Brands<span>|</span>Products<span>|</span>Contacts.</nav>
  <div class="copy">TOV Staffing © 2013. All Rights Reserved.</div>
</div>
</body>
</html>
```